Design Home Screen

We’re looking for talented UI/UX designers to create an eye-popping, modern, and fun Home Screen for the Plenk app — the future of real-time earned wage access and financial empowerment.
Your mission: make the Plenk experience come alive the moment users open the app.

Design Goals

The screen should instantly communicate energy, financial control, and trust.

The “Time on the Clock” and the “Plenk Balance” must be the stars of the screen — presented in a way that feels alive, interactive, and rewarding.

Think of how to visually celebrate a user’s progress at work and their earnings — something that makes checking the app feel fun and satisfying, not transactional.

Creative Direction

Style: Sleek, fintech-modern, with motion or visual elements that feel alive (micro-animations, glowing accents, gradient depth, or movement cues).

Tone: Confident, vibrant, and optimistic — this is a financial app that feels human and inspiring.

Color palette: Black, Gold, and Green, and any other color.

Typography: Clean, readable, and balanced between playful and professional.

Must-Have Elements

Time on the Clock – creatively displayed (e.g., countdown or progress animation as the user works).

Plenk Balance – bold, fun, and maybe even interactive (reflecting growth as the user earns).

A clean navigation structure for core tabs: Home, Access Pay, Boost, History, Profile.

Engaging micro-animations, icons, or progress indicators that make the user feel “in motion.”

Room for brand personality — the “Plenk” name and logo if desired.

```html
<!DOCTYPE html>
<html lang="en">
<head>
<meta charset="utf-8">
<title>Plenk – Home</title>
<link rel="stylesheet" href="https://fonts.googleapis.com/css2?family=Poppins:wght@300;400;500;600;700&display=swap">
<style>
  :root{
    --stage:#c9c9c9;
    --screen:#1c1c1c;
    --surface:#2b2b2b;
    --surface-2:#2f2f2f;
    --line:#424242;
    --gold:#d89d2b;
    --green:#79cd3c;
    --icon-green:#6cc24a;
    --text:#ffffff;
    --muted:#9a9a9a;
    --ink:#262626;
    --send-bg:#2f5b3a;
    --send-fg:#6fd08a;
    --pending-bg:#5a4a1c;
    --pending-fg:#e2a93a;
    --cancel-bg:#5c1e1e;
    --cancel-fg:#ff4a4a;
  }
  *{box-sizing:border-box;margin:0;padding:0}
  html,body{width:1200px;height:1034px;overflow:hidden}
  body{background:var(--stage);font-family:"Poppins",sans-serif;color:var(--text)}
  .screen{position:absolute;left:360px;top:0;width:480px;height:1034px;background:var(--screen);overflow:hidden}
  .abs{position:absolute}

  .status-time{left:22px;top:16px;font-size:19px;font-weight:600}
  .status-icons{right:20px;top:20px}

  .avatar{border-radius:50%;background:radial-gradient(circle at 45% 40%,#e8c2a8,#8a6a8e 70%,#3a3a3a);}
  .user-avatar{left:26px;top:63px;width:50px;height:50px;border:3px solid #3a3a3a}
  .brand{left:0;width:480px;top:70px;text-align:center;font-size:27px;font-weight:700;color:var(--gold);letter-spacing:.5px}
  .menu{right:28px;top:78px}

  .hello{left:23px;top:124px;font-size:14px;color:#bdbdbd}
  .user-name{left:23px;top:145px;font-size:24px;font-weight:600}

  .balance-card{left:23px;top:202px;width:435px;height:115px;background:var(--green);border-radius:14px;color:var(--ink)}
  .balance-label{position:absolute;left:22px;top:14px;font-size:20px;font-weight:400}
  .balance-amount{position:absolute;left:22px;top:44px;font-size:40px;font-weight:600;letter-spacing:-1px}
  .wallet-link{position:absolute;right:16px;top:74px;font-size:13.5px;display:flex;align-items:center;gap:10px}

  .info-card{top:343px;width:201px;height:131px;background:var(--surface);border-radius:10px}
  .pay-period{left:23px}
  .work-hours{left:257px}
  .card-title{position:absolute;left:13px;top:16px;font-size:13px;font-weight:500;display:flex;align-items:center;gap:5px;line-height:1.3}
  .period-month{position:absolute;left:13px;top:40px;font-size:20px;font-weight:500}
  .period-dates{position:absolute;left:13px;top:68px;font-size:13px}
  .rate{position:absolute;right:13px;top:19px;font-size:13px;color:var(--muted)}
  .hours-sub{position:absolute;left:13px;top:31px;font-size:13px}
  .digit{position:absolute;top:64px;width:47px;height:42px;border:1.5px solid #575757;background:#353535;border-radius:6px;color:var(--green);font-size:27px;font-weight:500;text-align:center;line-height:40px}
  .colon{position:absolute;left:72px;top:64px;font-size:24px;font-weight:600;line-height:38px}

  .actions{left:23px;top:500px;width:435px;height:110px}
  .action{position:absolute;top:0;width:71px;text-align:center}
  .action-tile{width:71px;height:71px;background:var(--surface);border-radius:10px;display:flex;align-items:center;justify-content:center}
  .action-label{position:absolute;top:77px;left:50%;transform:translateX(-50%);width:110px;font-size:13px;line-height:16px;text-align:center}

  .transactions{left:23px;top:639px;width:435px;height:420px;background:var(--surface-2);border:1px solid var(--line);border-radius:14px}
  .tx-head{position:absolute;left:26px;right:26px;top:22px;display:flex;justify-content:space-between;font-size:17px}
  .tx-row{position:absolute;left:0;right:0;height:75px;border-bottom:1px solid #3e3e3e}
  .tx-avatar{position:absolute;left:26px;top:12px;width:46px;height:46px;border:2px solid #555}
  .tx-name{position:absolute;left:88px;top:10px;font-size:17px}
  .tx-date{position:absolute;left:88px;top:38px;font-size:12.5px;color:#8b8b8b;word-spacing:2px}
  .tx-date span{margin-left:14px}
  .tx-amount{position:absolute;right:22px;top:10px;font-size:17px;font-weight:500}
  .badge{position:absolute;right:22px;top:35px;font-size:12.5px;padding:0 6px;border-radius:3px;line-height:18px}
  .badge.send{background:var(--send-bg);color:var(--send-fg)}
  .badge.pending{background:var(--pending-bg);color:var(--pending-fg)}
  .badge.cancel{background:var(--cancel-bg);color:var(--cancel-fg)}

  .tab-bar{left:0;top:920px;width:480px;height:114px;background:var(--surface-2);border-radius:20px 20px 0 0}
  .tab-indicator{position:absolute;left:40px;top:0;width:36px;height:3px;background:var(--gold);border-radius:2px}
  .tab{position:absolute;top:22px;width:90px;margin-left:-45px;text-align:center;font-size:13px;color:#d7d7d7}
  .tab svg{display:block;margin:0 auto 10px}
  .tab.active{color:var(--gold)}
</style>
</head>
<body>
<main class="screen">
  <div class="abs status-time">9:41</div>
  <svg class="abs status-icons" width="86" height="16" viewBox="0 0 86 16" aria-hidden="true">
    <rect x="0" y="10" width="3" height="5" rx="1" fill="#fff"/><rect x="5" y="7" width="3" height="8" rx="1" fill="#fff"/><rect x="10" y="4" width="3" height="11" rx="1" fill="#fff"/><rect x="15" y="1" width="3" height="14" rx="1" fill="#777"/>
    <path d="M28 6a11 11 0 0 1 15 0M31 9a6.5 6.5 0 0 1 9 0" stroke="#fff" stroke-width="2" fill="none" stroke-linecap="round"/><circle cx="35.5" cy="12.5" r="1.8" fill="#fff"/>
    <rect x="54" y="2" width="28" height="12" rx="3.5" fill="none" stroke="#888"/><rect x="56" y="4" width="24" height="8" rx="2" fill="#fff"/><rect x="83" y="6" width="2" height="4" rx="1" fill="#888"/>
  </svg>

  <div class="abs avatar user-avatar" role="img" aria-label="User profile avatar"></div>
  <div class="abs brand">PLENK</div>
  <svg class="abs menu" width="30" height="22" viewBox="0 0 30 22" aria-hidden="true">
    <g stroke="var(--gold)" stroke-width="3.5" stroke-linecap="round"><path d="M10 2h18M2 11h26M12 20h12"/></g>
  </svg>

  <div class="abs hello">Hello!</div>
  <div class="abs user-name">Tovakmir</div>

  <section class="abs balance-card">
    <div class="balance-label">Plenk Wage Balance:</div>
    <div class="balance-amount">$2,619.89</div>
    <div class="wallet-link">My Wallet
      <svg width="24" height="14" viewBox="0 0 24 14" aria-hidden="true"><path d="M1 7h21M16 1l6 6-6 6" stroke="#262626" stroke-width="2" fill="none" stroke-linecap="round" stroke-linejoin="round"/></svg>
    </div>
  </section>

  <section class="abs info-card pay-period">
    <div class="card-title">
      <svg width="11" height="11" viewBox="0 0 12 12" aria-hidden="true"><rect x="1" y="2" width="10" height="9" rx="1.5" stroke="#fff" fill="none"/><path d="M1 5h10M4 1v2M8 1v2" stroke="#fff"/></svg>
      Current Pay Period
    </div>
    <div class="period-month">March</div>
    <div class="period-dates">1-15, 2025</div>
  </section>

  <section class="abs info-card work-hours">
    <div class="card-title">
      <svg width="11" height="11" viewBox="0 0 12 12" aria-hidden="true"><circle cx="6" cy="6" r="5" stroke="#fff" fill="none"/><path d="M6 3v3l2 1" stroke="#fff" fill="none"/></svg>
      Work Hours
    </div>
    <div class="hours-sub">Spending Hours</div>
    <div class="rate">$20.00/hr</div>
    <div class="digit" style="left:13px">19</div>
    <div class="colon">:</div>
    <div class="digit" style="left:91px">00</div>
  </section>

  <nav class="abs actions">
    <div class="action" style="left:0">
      <div class="action-tile">
        <svg width="34" height="34" viewBox="0 0 34 34" aria-hidden="true"><g stroke="var(--icon-green)" stroke-width="2" fill="none" stroke-linecap="round"><path d="M20 5H6a2 2 0 0 0-2 2v22a2 2 0 0 0 2 2h20a2 2 0 0 0 2-2V16"/><circle cx="26" cy="7" r="4"/><path d="M9 15h10M9 20h13M9 25h8"/></g></svg>
      </div>
      <div class="action-label">Request<br>Money</div>
    </div>
    <div class="action" style="left:117px">
      <div class="action-tile">
        <svg width="34" height="34" viewBox="0 0 34 34" aria-hidden="true"><g stroke="var(--icon-green)" stroke-width="2" fill="none" stroke-linecap="round" stroke-linejoin="round"><path d="M12 4h10l-3 6h-4z"/><path d="M15 10c-6 4-9 9-9 14a6 6 0 0 0 6 6h10a6 6 0 0 0 6-6c0-5-3-10-9-14"/><path d="M20 17h-4a2 2 0 0 0 0 4h2a2 2 0 0 1 0 4h-4M17 15v2M17 25v2"/></g></svg>
      </div>
      <div class="action-label">Loan<br>Access</div>
    </div>
    <div class="action" style="left:235px">
      <div class="action-tile">
        <svg width="34" height="34" viewBox="0 0 34 34" aria-hidden="true"><g stroke="var(--icon-green)" stroke-width="2.2" fill="none" stroke-linecap="round" stroke-linejoin="round"><path d="M5 17a12 12 0 0 1 21-8M29 17a12 12 0 0 1-21 8"/><path d="M26 3v6h-6M8 31v-6h6"/></g></svg>
      </div>
      <div class="action-label">Updated<br>Employment</div>
    </div>
    <div class="action" style="left:359px">
      <div class="action-tile">
        <svg width="36" height="34" viewBox="0 0 36 34" aria-hidden="true"><g stroke="var(--icon-green)" stroke-width="2" fill="none" stroke-linecap="round" stroke-linejoin="round"><path d="M4 14h26v16H4z"/><path d="M22 19h8v6h-8z"/><path d="M8 14a9 9 0 0 1 18 0"/><path d="M23 2v6M20 5l3 3 3-3M30 2v6M27 5l3 3 3-3M16 3v4"/></g></svg>
      </div>
      <div class="action-label">Earn<br>$7,522.63</div>
    </div>
  </nav>

  <section class="abs transactions">
    <div class="tx-head"><span>Recent transactions</span><span>View all</span></div>
    <div class="tx-row" style="top:60px">
      <div class="avatar tx-avatar" role="img" aria-label="Company contact photo"></div>
      <div class="tx-name">Jhon Doe Inc</div>
      <div class="tx-date">17 Sep 2023<span>11:21 AM</span></div>
      <div class="tx-amount">$ 350.00</div>
      <div class="badge send">Send</div>
    </div>
    <div class="tx-row" style="top:135px">
      <div class="avatar tx-avatar" role="img" aria-label="Company contact photo"></div>
      <div class="tx-name">Task Harbor</div>
      <div class="tx-date">17 Sep 2023<span>10:34 AM</span></div>
      <div class="tx-amount">$ 100.00</div>
      <div class="badge pending">Pending</div>
    </div>
    <div class="tx-row" style="top:210px">
      <div class="avatar tx-avatar" role="img" aria-label="Company contact photo"></div>
      <div class="tx-name">Velora Inc.</div>
      <div class="tx-date">16 Sep 2023<span>16:08 PM</span></div>
      <div class="tx-amount">$ 1.75</div>
      <div class="badge cancel">Cancel</div>
    </div>
  </section>

  <nav class="abs tab-bar">
    <div class="tab-indicator"></div>
    <div class="tab active" style="left:59px">
      <svg width="32" height="32" viewBox="0 0 32 32" aria-hidden="true"><path d="M4 14 16 4l12 10v14H20v-8h-8v8H4z" stroke="var(--gold)" stroke-width="2.2" fill="none" stroke-linejoin="round"/></svg>Home
    </div>
    <div class="tab" style="left:148px">
      <svg width="32" height="32" viewBox="0 0 32 32" aria-hidden="true"><g stroke="#d7d7d7" stroke-width="2" fill="none"><rect x="3" y="7" width="26" height="18" rx="2"/><path d="M3 12h26"/><path d="M7 20h3" stroke-linecap="round"/></g></svg>Access Pay
    </div>
    <div class="tab" style="left:242px">
      <svg width="32" height="32" viewBox="0 0 32 32" aria-hidden="true"><g stroke="#d7d7d7" stroke-width="2" fill="none" stroke-linejoin="round"><circle cx="16" cy="16" r="13"/><path d="M18 7l-7 10h5l-2 8 7-10h-5z"/></g></svg>Boost
    </div>
    <div class="tab" style="left:332px">
      <svg width="32" height="32" viewBox="0 0 32 32" aria-hidden="true"><g stroke="#d7d7d7" stroke-width="2" fill="none" stroke-linecap="round"><path d="M5 16a11 11 0 1 0 3-8"/><path d="M4 4v6h6M16 10v6l4 3"/></g></svg>History
    </div>
    <div class="tab" style="left:418px">
      <svg width="32" height="32" viewBox="0 0 32 32" aria-hidden="true"><g stroke="#d7d7d7" stroke-width="2" fill="none"><circle cx="16" cy="10" r="6"/><path d="M5 29v-3a7 7 0 0 1 7-7h8a7 7 0 0 1 7 7v3z" stroke-linejoin="round"/></g></svg>Profile
    </div>
  </nav>
</main>
</body>
</html>
```